Bao Lotus Menu Design Project

This project is pretty straight forward. You will be given 3 files which include the following:
1. Our proposed menu
2. Our Company logo
3. A sample menu on what we are looking for design wise

Your job is to create a visually pleasing menu that is simple, clean and fresh. Please refer to our home website for additional information. (www.baolotus-example.com) Must be in eps or equivalent format.

Target Market(s)

20s to 40s

Industry/Entity Type

It Company

Requirements
Must have
• Company log
Must be in EPS format

```html
<!DOCTYPE html>
<html lang="en">
<head>
<meta charset="utf-8">
<title>Bao Lotus Menu</title>
<link rel="stylesheet" href="https://fonts.googleapis.com/css2?family=Oswald:wght@500;700&family=Open+Sans:wght@400;600&display=swap">
<style>
  :root {
    --page-bg: #e9e6e1;
    --board-light: #3a3a3b;
    --board-dark: #161617;
    --chalk: #f2f2f2;
    --chalk-soft: #c9c9c9;
    --brand-red: #d6211c;
    --food-warm: #c9822f;
    --food-pale: #d9b77a;
    --food-green: #3d4f2c;
  }
  * { margin: 0; padding: 0; box-sizing: border-box; }
  html, body { width: 1091px; height: 1200px; overflow: hidden; }
  body { background: var(--page-bg); position: relative; font-family: "Open Sans", sans-serif; }

  .menu-board {
    position: absolute; left: 148px; top: 80px; width: 794px; height: 1040px;
    background: radial-gradient(ellipse at 50% 40%, var(--board-light), var(--board-dark) 85%);
    color: var(--chalk);
    box-shadow: 0 6px 18px rgba(0,0,0,.35);
  }
  .section-title {
    position: absolute; left: 0; width: 100%; text-align: center;
    font-family: "Oswald", sans-serif; font-weight: 700; font-size: 38px;
    letter-spacing: 3px; text-transform: uppercase;
  }
  .title-dim-sum { top: 40px; }
  .title-starters { top: 480px; }

  .menu-grid {
    position: absolute; left: 30px; width: 734px;
    display: grid; grid-template-columns: repeat(3, 1fr); column-gap: 20px;
  }
  .dim-sum-grid { top: 115px; row-gap: 40px; }
  .starters-grid { top: 555px; }

  .menu-item { text-align: center; }
  .item-name { font-family: "Oswald", sans-serif; font-weight: 500; font-size: 18px; letter-spacing: .5px; }
  .item-price { font-size: 14px; font-weight: 600; margin: 2px 0 6px; }
  .item-desc { font-size: 13px; line-height: 1.45; color: var(--chalk-soft); padding: 0 12px; }

  .specials-note {
    position: absolute; left: 0; top: 705px; width: 100%; text-align: center;
    font-family: "Oswald", sans-serif; font-weight: 500; font-size: 18px; letter-spacing: 1px;
  }
  .allergy-note {
    position: absolute; left: 130px; top: 750px; width: 534px; text-align: center;
    font-size: 13px; line-height: 1.5; color: var(--chalk-soft);
  }

  .food-photo { position: absolute; top: 885px; height: 100px; }
  .photo-wings { left: 22px; width: 186px; border-radius: 50%; background: radial-gradient(ellipse, var(--food-warm), #8a4a1a 70%, #ddd 72%); }
  .photo-rolls { left: 215px; width: 170px; top: 875px; height: 95px; background: linear-gradient(160deg, var(--food-pale), #a9793d); }
  .photo-greens { left: 390px; width: 136px; top: 880px; height: 95px; border-radius: 6px; background: radial-gradient(ellipse, var(--food-green), #1c2414 75%, #eee 78%); }

  .brand-block {
    position: absolute; left: 548px; top: 870px; width: 220px; height: 130px;
    display: flex; align-items: center; justify-content: center; gap: 12px;
  }
  .brand-mark { width: 22px; height: 22px; border-radius: 50%; background: var(--brand-red); }
  .brand-name {
    font-family: "Oswald", sans-serif; font-weight: 700; font-size: 40px;
    color: var(--brand-red); text-transform: uppercase; line-height: 1;
  }
</style>
</head>
<body>
  <main class="menu-board">
    <h2 class="section-title title-dim-sum">Dim Sum</h2>
    <section class="menu-grid dim-sum-grid">
      <article class="menu-item"><h3 class="item-name">Pork Siu Mai</h3><p class="item-price">$6.50</p><p class="item-desc">Steamed pork and shrimp dumplings, four pieces</p></article>
      <article class="menu-item"><h3 class="item-name">Shrimp Har Gow</h3><p class="item-price">$7.00</p><p class="item-desc">Crystal shrimp dumplings, four pieces</p></article>
      <article class="menu-item"><h3 class="item-name">Char Siu Bao</h3><p class="item-price">$6.00</p><p class="item-desc">Fluffy steamed buns with barbecue pork</p></article>
      <article class="menu-item"><h3 class="item-name">Potstickers</h3><p class="item-price">$6.50</p><p class="item-desc">Pan-fried pork and cabbage dumplings, six pieces</p></article>
      <article class="menu-item"><h3 class="item-name">Spring Rolls</h3><p class="item-price">$5.50</p><p class="item-desc">Crisp vegetable rolls with sweet chili dipping sauce</p></article>
      <article class="menu-item"><h3 class="item-name">Bao</h3><p class="item-price">$4.50</p><p class="item-desc">Pork belly, pickles and crushed peanuts</p></article>
      <article class="menu-item"><h3 class="item-name">Wontons</h3><p class="item-price">$6.00</p><p class="item-desc">Chili oil wontons with spring onion</p></article>
      <article class="menu-item"><h3 class="item-name">Gyoza</h3><p class="item-price">$6.50</p><p class="item-desc">Chicken and chive dumplings, seared golden</p></article>
      <article class="menu-item"><h3 class="item-name">Lotus Leaf Rice</h3><p class="item-price">$7.50</p><p class="item-desc">Sticky rice with chicken and mushroom, steamed in lotus leaf</p></article>
    </section>

    <h2 class="section-title title-starters">Starters</h2>
    <section class="menu-grid starters-grid">
      <article class="menu-item"><h3 class="item-name">Edamame</h3><p class="item-price">$4.00</p><p class="item-desc">Sea salt or spicy garlic</p></article>
      <article class="menu-item"><h3 class="item-name">Salt &amp; Pepper Calamari</h3><p class="item-price">$8.50</p><p class="item-desc">Lightly fried squid with chili and scallion</p></article>
      <article class="menu-item"><h3 class="item-name">Crispy Sesame Chicken</h3><p class="item-price">$9.00</p><p class="item-desc">Tossed in honey sesame glaze, served with steamed rice</p></article>
    </section>

    <p class="specials-note">Ask about our daily specials</p>
    <p class="allergy-note">Please let your server know of any food allergies. All dishes are prepared fresh to order and may contain nuts, soy or gluten.</p>

    <div class="food-photo photo-wings" role="img" aria-label="Photo of crispy glazed chicken on a white plate"></div>
    <div class="food-photo photo-rolls" role="img" aria-label="Photo of golden fried spring rolls"></div>
    <div class="food-photo photo-greens" role="img" aria-label="Photo of sautéed greens in a white dish"></div>

    <div class="brand-block">
      <span class="brand-mark"></span>
      <span class="brand-name">Bao Lotus</span>
    </div>
  </main>
</body>
</html>
```